Business Card Design

We require a business card design for a law firm, our signature colours are maroon and cream. Our slogan is "From our family to yours", we would like the cards to be professional however feminine at the same time.

Industry/Entity Type

Business

Contact Information for Business Card

Helena Brockett & Associates Lawyers & Conveyancers, Helena Brockett LL.B. Principal Solicitor, 17 Thornbury Street, Kelvale NSW 2239

Logo styles of interest
Emblem Logo
Abstract Logo
Wordmark Logo

```html
<!DOCTYPE html>
<html lang="en">
<head>
<meta charset="utf-8">
<title>Helena Brockett &amp; Associates — Business Card</title>
<link rel="stylesheet" href="https://fonts.googleapis.com/css2?family=Dancing+Script:wght@500&family=Tinos&display=swap">
<style>
  :root {
    --maroon: #7f1a12;
    --cream: #fdf6d6;
    --emblem-tint: rgba(253, 246, 214, 0.22);
  }
  * { margin: 0; padding: 0; box-sizing: border-box; }
  html, body { width: 1200px; height: 726px; overflow: hidden; background: var(--maroon); }
  .card {
    position: relative;
    width: 1200px;
    height: 726px;
    background: var(--maroon);
    color: var(--cream);
    font-family: "Tinos", "Times New Roman", serif;
  }
  .emblem {
    position: absolute;
    left: 220px;
    top: 20px;
    width: 363px;
    height: 357px;
    background: var(--emblem-tint);
    border-radius: 6px;
  }
  .slogan {
    position: absolute;
    left: 640px;
    top: 40px;
    font-family: "Dancing Script", cursive;
    font-weight: 500;
    font-size: 54px;
    line-height: 1;
    white-space: nowrap;
  }
  .firm-name {
    position: absolute;
    left: 0;
    top: 398px;
    width: 750px;
    text-align: center;
    font-size: 45px;
    line-height: 63px;
    font-weight: 400;
  }
  .principal, .address {
    position: absolute;
    font-size: 33px;
    line-height: 43px;
    white-space: nowrap;
  }
  .principal { left: 86px; top: 584px; }
  .address { left: 812px; top: 592px; }
</style>
</head>
<body>
  <main class="card">
    <div class="emblem" role="img" aria-label="Ornate scales of justice emblem with flourished base"></div>

    <p class="slogan">From our family to yours</p>

    <h1 class="firm-name">Helena Brockett &amp; Associates<br>Lawyers &amp; Conveyancers</h1>

    <p class="principal">Helena Brockett LL.B.<br>Principal Solicitor</p>

    <address class="address" style="font-style: normal;">17 Thornbury Street<br>Kelvale NSW 2239</address>
  </main>
</body>
</html>
```